San Francisco Hotel in need of banner ad set

We need a banner ad set for our new hotel in San Francisco called 'The Marigold Crestview'. The Marigold Crestview is joining our 'Bluewren Lodgings' portfolio of hotels. The final design should communicate 'Now a Piece of Bluewren Lodgings' and our introductory 15% discount.

Here are the details of the promotion:

http://mari.preview.tolvanek.com/promotions/welcome-to-bluewren-lodgings.htm

Ads are fixed (no flash, no animation)

Ad Dimensions:
120x120
160x600
300x250
728x90

Target Market(s)

Customers who have researched rates on our website and plan to travel to San Francisco. These ads will remarket our hotel to them after leaving our site.

Industry/Entity Type

Hotel

Font styles to use
Serif

Colors
ec1f27
faee3f

Requirements
Must have
• Check Availability button
The Marigold Crestview logo (attached both black and white depending on what you need)
Bluewren Lodgings logo
15% Off

Sub text:
No up front charges
24 hour cancellations
Nice to have
• No up front charges
24 hour cancellations

```html
<!DOCTYPE html>
<html lang="en">
<head>
<meta charset="utf-8">
<title>The Marigold Crestview – Banner Ad Set</title>
<link href="https://fonts.googleapis.com/css2?family=Open+Sans:wght@600;700&family=Arimo:wght@400;700&display=swap" rel="stylesheet">
<style>
  :root{
    --brand-red:#ec1f27;
    --brand-yellow:#faee3f;
    --button-yellow:#fbe93a;
    --ink:#1e1e1e;
    --white:#ffffff;
    --backdrop-dark:#2a140b;
    --backdrop-mid:#4a2414;
    --photo-sky:#6f8fb4;
    --photo-stone:#d9d3c6;
    --photo-street:#3a3330;
  }
  html,body{margin:0;padding:0;width:1200px;height:801px;overflow:hidden;}
  body{
    background:linear-gradient(100deg,var(--backdrop-dark) 0%,var(--backdrop-mid) 45%,var(--backdrop-dark) 100%);
    font-family:"Open Sans",Arial,sans-serif;
  }
  .stage{position:absolute;left:0;top:0;width:1016px;height:678px;transform:scale(1.1811);transform-origin:0 0;}
  .ad{position:absolute;overflow:hidden;background:var(--brand-red);color:var(--white);}
  .ad *{box-sizing:border-box;}
  .abs{position:absolute;}
  .center{left:0;right:0;text-align:center;}
  .logo-panel{background:var(--white);}
  .brand-name{color:var(--ink);font-family:"Open Sans",Arial,sans-serif;font-weight:700;white-space:nowrap;letter-spacing:-0.2px;}
  .partner{display:flex;align-items:center;justify-content:center;gap:4px;}
  .partner-dot{width:16px;height:16px;border-radius:50%;background:var(--brand-yellow);flex:none;}
  .partner-name{font-weight:700;color:var(--white);font-size:8px;line-height:1.05;text-transform:uppercase;text-align:left;}
  .headline{font-weight:600;text-transform:uppercase;line-height:1.05;letter-spacing:-0.3px;white-space:nowrap;}
  .accent{color:var(--brand-yellow);}
  .offer{font-weight:700;line-height:1;letter-spacing:-0.5px;white-space:nowrap;}
  .rates{font-weight:600;text-transform:uppercase;line-height:1.05;letter-spacing:-0.3px;white-space:nowrap;}
  .terms{font-family:"Arimo",Arial,sans-serif;font-size:11px;line-height:1.3;white-space:nowrap;}
  .photo{background:linear-gradient(180deg,var(--photo-sky) 0%,var(--photo-stone) 30%,var(--photo-stone) 78%,var(--photo-street) 100%);}
  .cta{
    display:flex;align-items:center;justify-content:space-between;
    background:var(--button-yellow);color:var(--ink);border-radius:3px;
    font-family:"Arimo",Arial,sans-serif;font-weight:700;font-size:12px;white-space:nowrap;
    padding:0 5px 0 7px;box-shadow:0 1px 2px rgba(0,0,0,.35);
  }
  .cta-arrow{width:13px;height:13px;border-radius:50%;background:#333;display:flex;align-items:center;justify-content:center;}
</style>
</head>
<body>
<div class="stage">

  <!-- 160 x 600 skyscraper -->
  <div class="ad skyscraper" style="left:46px;top:37px;width:160px;height:600px;">
    <div class="abs logo-panel" style="left:0;top:0;width:160px;height:56px;display:flex;align-items:center;justify-content:center;">
      <span class="brand-name" style="font-size:11.5px;">The Marigold Crestview</span>
    </div>
    <div class="abs center headline" style="top:69px;font-size:19px;">Downtown<br><span class="accent">San Francisco</span></div>
    <div class="abs center headline" style="top:116px;font-size:12px;">Now a piece of<br>Bluewren Lodgings</div>
    <div class="abs center partner" style="top:166px;">
      <span class="partner-dot" style="width:30px;height:30px;"></span>
      <span class="partner-name">Bluewren<br>Lodgings</span>
    </div>
    <div class="abs center offer" style="top:212px;font-size:27px;">15% OFF</div>
    <div class="abs center rates" style="top:240px;font-size:19px;">Room Rates</div>
    <div class="abs photo" role="img" aria-label="Photo of the hotel's white facade on a downtown street corner at dusk" style="left:0;top:272px;width:160px;height:256px;"></div>
    <svg class="abs" style="left:0;top:268px;" width="160" height="40" viewBox="0 0 160 40" aria-hidden="true">
      <path d="M0 0H160V28C110 10 50 6 0 22Z" fill="var(--brand-red)"/>
      <path d="M0 22C50 6 110 10 160 28V34C110 16 50 12 0 28Z" fill="var(--brand-yellow)"/>
    </svg>
    <div class="abs center terms" style="top:534px;">No up front charges<br>24 hour cancellations</div>
    <div class="abs cta" style="left:15px;top:567px;width:129px;height:24px;">Check Availability
      <span class="cta-arrow"><svg width="7" height="7" viewBox="0 0 7 7"><path d="M2 1l3 2.5L2 6" stroke="#fff" stroke-width="1.5" fill="none"/></svg></span>
    </div>
  </div>

  <!-- 728 x 90 leaderboard -->
  <div class="ad leaderboard" style="left:226px;top:37px;width:728px;height:90px;">
    <div class="abs logo-panel" style="left:0;top:0;width:164px;height:90px;">
      <div class="abs center brand-name" style="top:20px;font-size:11.5px;">The Marigold Crestview</div>
      <div class="abs cta" style="left:15px;top:57px;width:130px;height:23px;">Check Availability
        <span class="cta-arrow"><svg width="7" height="7" viewBox="0 0 7 7"><path d="M2 1l3 2.5L2 6" stroke="#fff" stroke-width="1.5" fill="none"/></svg></span>
      </div>
    </div>
    <div class="abs headline" style="left:164px;width:300px;text-align:center;top:7px;font-size:17px;">Downtown <span class="accent">San Francisco</span></div>
    <div class="abs headline" style="left:164px;width:300px;text-align:center;top:31px;font-size:12px;">Now a piece of Bluewren Lodgings</div>
    <span class="abs partner-dot" style="left:186px;top:57px;width:26px;height:26px;"></span>
    <div class="abs offer" style="left:224px;top:58px;font-size:19px;">15% OFF ROOM RATES</div>
    <div class="abs photo" role="img" aria-label="Photo of the hotel facade and street with passing cars" style="left:466px;top:0;width:262px;height:90px;"></div>
    <svg class="abs" style="left:456px;top:0;" width="16" height="90" viewBox="0 0 16 90" aria-hidden="true">
      <path d="M0 0H6C2 30 2 60 6 90H0Z" fill="var(--brand-red)"/>
      <path d="M6 0H12C8 30 8 60 12 90H6C2 60 2 30 6 0Z" fill="var(--brand-yellow)"/>
    </svg>
    <div class="abs terms" style="left:489px;top:72px;font-size:11px;color:var(--white);">No up front charges&nbsp;&nbsp;&nbsp;&nbsp;24 hour cancellations</div>
  </div>

  <!-- 300 x 250 medium rectangle -->
  <div class="ad rectangle" style="left:227px;top:141px;width:300px;height:250px;">
    <div class="abs photo" role="img" aria-label="Photo of the hotel's white multi-storey facade" style="left:150px;top:0;width:150px;height:250px;"></div>
    <svg class="abs" style="left:145px;top:0;" width="30" height="250" viewBox="0 0 30 250" aria-hidden="true">
      <path d="M0 0H18C4 80 4 170 12 250H0Z" fill="var(--brand-red)"/>
      <path d="M12 250C4 170 4 80 18 0H25C11 80 11 170 19 250Z" fill="var(--brand-yellow)"/>
    </svg>
    <div class="abs headline" style="left:10px;top:6px;font-size:19px;letter-spacing:-0.5px;">Downtown<br><span class="accent">San Francisco</span></div>
    <div class="abs headline" style="left:10px;top:54px;font-size:12px;">Now a piece of<br>Bluewren Lodgings</div>
    <span class="abs partner-dot" style="left:57px;top:93px;width:28px;height:28px;"></span>
    <div class="abs offer" style="left:10px;width:122px;text-align:center;top:128px;font-size:27px;">15% OFF</div>
    <div class="abs rates" style="left:10px;width:122px;text-align:center;top:155px;font-size:19px;">Room Rates</div>
    <div class="abs terms" style="left:10px;width:122px;text-align:center;top:184px;">No up front charges<br>24 hour cancellations</div>
    <div class="abs cta" style="left:7px;top:218px;width:129px;height:23px;">Check Availability
      <span class="cta-arrow"><svg width="7" height="7" viewBox="0 0 7 7"><path d="M2 1l3 2.5L2 6" stroke="#fff" stroke-width="1.5" fill="none"/></svg></span>
    </div>
    <div class="abs logo-panel" style="left:164px;top:210px;width:136px;height:40px;display:flex;align-items:center;justify-content:center;">
      <span class="brand-name" style="font-size:10px;">The Marigold Crestview</span>
    </div>
  </div>

  <!-- 120 x 120 square -->
  <div class="ad square" style="left:227px;top:411px;width:120px;height:120px;">
    <div class="abs logo-panel" style="left:0;top:0;width:120px;height:40px;display:flex;align-items:center;justify-content:center;">
      <span class="brand-name" style="font-size:8.5px;">The Marigold Crestview</span>
    </div>
    <div class="abs center headline" style="top:46px;font-size:10px;">Now a piece of<br>Bluewren Lodgings</div>
    <div class="abs photo" role="img" aria-label="Photo of the hotel facade, darkened behind the offer" style="left:0;top:73px;width:120px;height:47px;background:linear-gradient(180deg,#5a5550,#2e2a28);"></div>
    <div class="abs center offer" style="top:76px;font-size:17px;">15% OFF</div>
    <div class="abs center rates" style="top:96px;font-size:12px;">Room Rates</div>
  </div>

</div>
</body>
</html>
```